Ciel doux

Hello,
I’m a designer sunglasses reatail Store owner in Montreal, Quebec.

Looking for something modern, fresh with a trendy appeal.

Will send my logo.
Thank you.

Store

```html
<!DOCTYPE html>
<html lang="fr">
<head>
<meta charset="utf-8">
<title>Ciel doux – carte professionnelle</title>
<link rel="stylesheet" href="https://fonts.googleapis.com/css2?family=Lato:wght@300;400;700&display=swap">
<style>
  :root {
    --page: #e9e6e2;
    --card-top: #f4f4f4;
    --card-bottom: #e2e1e0;
    --ink: #2a2a2a;
    --black: #141414;
    --red: #a5232b;
    --contact: #b3a088;
  }
  * { margin: 0; padding: 0; box-sizing: border-box; }
  html, body {
    width: 1200px;
    height: 970px;
    overflow: hidden;
    background: var(--page);
    font-family: "Lato", sans-serif;
  }
  .business-card {
    position: absolute;
    left: 80px;
    top: 190px;
    width: 1040px;
    height: 590px;
    border-radius: 34px;
    overflow: hidden;
    background: linear-gradient(160deg, var(--card-top) 0%, #ececec 45%, var(--card-bottom) 100%);
    box-shadow: 0 18px 40px rgba(0, 0, 0, 0.18);
  }
  .card-band {
    position: absolute;
    left: 0;
    right: 0;
    bottom: 0;
    height: 230px;
    background: linear-gradient(100deg, var(--red) 0%, #4a1c1f 35%, var(--black) 65%, var(--black) 100%);
  }
  .brand {
    position: absolute;
    left: 55px;
    top: 92px;
    display: flex;
    align-items: center;
    gap: 22px;
  }
  .brand-dot {
    width: 64px;
    height: 64px;
    border-radius: 50%;
    background: var(--red);
  }
  .brand-name {
    font-size: 64px;
    font-weight: 700;
    letter-spacing: 3px;
    color: var(--ink);
    text-transform: uppercase;
  }
  .person {
    position: absolute;
    left: 53px;
    top: 288px;
  }
  .person-name {
    font-size: 36px;
    font-weight: 700;
    color: var(--ink);
    line-height: 1.1;
  }
  .person-role {
    font-size: 27px;
    font-weight: 400;
    color: var(--red);
    line-height: 1.2;
  }
  .contact-list {
    position: absolute;
    right: 42px;
    top: 392px;
    list-style: none;
  }
  .contact-item {
    display: flex;
    justify-content: flex-end;
    align-items: center;
    gap: 12px;
    height: 35px;
    font-size: 26px;
    font-weight: 300;
    color: var(--contact);
  }
  .contact-icon {
    width: 28px;
    height: 28px;
    flex: none;
  }
</style>
</head>
<body>
  <main class="business-card">
    <div class="card-band" role="img" aria-label="Bande décorative rouge et noire en bas de la carte"></div>

    <header class="brand">
      <span class="brand-dot"></span>
      <span class="brand-name">Ciel doux</span>
    </header>

    <section class="person">
      <p class="person-name">Marc Dubois</p>
      <p class="person-role">Fondateur</p>
    </section>

    <ul class="contact-list">
      <li class="contact-item">(514) 555-0148
        <svg class="contact-icon" viewBox="0 0 28 28" aria-label="mobile"><rect width="28" height="28" rx="4" fill="var(--red)"/><rect x="9" y="5" width="10" height="18" rx="1.5" fill="none" stroke="#fff" stroke-width="1.8"/><rect x="11" y="8" width="6" height="5" fill="#fff"/></svg>
      </li>
      <li class="contact-item">(514) 555-0149
        <svg class="contact-icon" viewBox="0 0 28 28" aria-label="téléphone"><rect width="28" height="28" rx="4" fill="var(--red)"/><path d="M6,12 C6,7 22,7 22,12 L19,13 L18,11 L10,11 L9,13 Z" fill="#fff"/><rect x="8" y="14" width="12" height="8" rx="1.5" fill="#fff"/><circle cx="14" cy="18" r="2" fill="var(--red)"/></svg>
      </li>
      <li class="contact-item">info@cieldoux.ca
        <svg class="contact-icon" viewBox="0 0 28 28" aria-label="courriel"><rect width="28" height="28" rx="4" fill="var(--red)"/><rect x="5" y="8" width="18" height="12" fill="#fff"/><path d="M5,8 L14,15 L23,8 M5,20 L11,13 M23,20 L17,13" fill="none" stroke="var(--red)" stroke-width="1.4"/></svg>
      </li>
      <li class="contact-item">www.cieldoux.ca
        <svg class="contact-icon" viewBox="0 0 28 28" aria-label="site web"><rect width="28" height="28" rx="4" fill="var(--red)"/><g fill="none" stroke="#fff" stroke-width="1.5"><circle cx="14" cy="14" r="8"/><ellipse cx="14" cy="14" rx="3.5" ry="8"/><path d="M6,14 H22 M7.5,10 H20.5 M7.5,18 H20.5"/></g></svg>
      </li>
    </ul>
  </main>
</body>
</html>
```